Marrowick Billboards

We already hava a logo, slogan and general theme, we are looking for 2 to 3 billboard designs for out Recreational-Use Retail Cannabis Dispensary in NY state. We would like for the billboard to be a "Space" theme with a realistic-looking astronaut, we cannot have any "cartoon-like" images that would be attractive to children per state regulations. We would like the following wording included:
Marrowick Cannabis Company - Oswego , slogan is "Products out of this world" , address of 871 Tallow Lane - Oswego, Free Delivery - Orders over $150 . Our primary brand color is lime green.

```html
<!DOCTYPE html>
<html lang="en">
<head>
<meta charset="utf-8">
<title>Marrowick Cannabis Company – Billboard</title>
<link rel="stylesheet" href="https://fonts.googleapis.com/css2?family=Cinzel:wght@500&family=EB+Garamond:wght@400&family=Barlow+Condensed:ital,wght@1,700&display=swap">
<style>
  :root {
    --page-bg: #d9dadc;
    --space-deep: #05070d;
    --space-mid: #0d1a33;
    --photo-grey: #9da4b0;
    --photo-blue: #2a5d9c;
    --lime: #6cc043;
    --lime-bright: #8fd14f;
    --lime-yellow: #c2e23a;
    --ink-black: #050505;
    --white: #ffffff;
  }
  * { margin: 0; padding: 0; box-sizing: border-box; }
  html, body {
    width: 1200px;
    height: 1122px;
    overflow: hidden;
    background: var(--page-bg);
  }
  .billboard {
    position: absolute;
    left: 50px;
    top: 401px;
    width: 1100px;
    height: 321px;
    overflow: hidden;
    background:
      radial-gradient(ellipse at 20% 25%, rgba(40,70,130,0.45), transparent 60%),
      linear-gradient(180deg, var(--space-mid), var(--space-deep));
  }
  .hero-photo {
    position: absolute;
    left: 397px;
    top: 0;
    width: 703px;
    height: 321px;
    background: linear-gradient(100deg,
      rgba(13,26,51,0) 0%,
      rgba(157,164,176,0.55) 14%,
      rgba(157,164,176,0.45) 38%,
      rgba(42,93,156,0.55) 62%,
      rgba(13,26,51,0.35) 100%);
  }
  .headline-rule {
    position: absolute;
    top: 93px;
    height: 2px;
    background: var(--lime);
  }
  .headline-rule.left { left: 67px; width: 116px; }
  .headline-rule.right { left: 227px; width: 115px; }
  .rule-mark {
    position: absolute;
    left: 197px;
    top: 80px;
    width: 16px;
    height: 16px;
    border-radius: 50%;
    background: var(--lime);
  }
  .headline {
    position: absolute;
    left: 0;
    top: 108px;
    width: 410px;
    text-align: center;
    font-family: "EB Garamond", serif;
    font-weight: 400;
    color: var(--white);
    text-transform: uppercase;
    line-height: 1;
  }
  .headline .line { display: block; font-size: 54px; letter-spacing: 1px; }
  .headline .line + .line { margin-top: -6px; }
  .headline .accent {
    display: block;
    font-size: 84px;
    margin-top: -4px;
    background: linear-gradient(90deg, var(--lime), var(--lime-yellow));
    -webkit-background-clip: text;
    background-clip: text;
    color: transparent;
  }
  .brand {
    position: absolute;
    left: 740px;
    top: 30px;
    width: 342px;
    text-align: center;
    font-family: "Cinzel", serif;
    font-weight: 500;
    color: var(--white);
    line-height: 1;
  }
  .brand-name { display: block; font-size: 40px; }
  .brand-sub { display: block; font-size: 23px; margin-top: 2px; }
  .address {
    position: absolute;
    left: 740px;
    top: 104px;
    width: 342px;
    display: flex;
    justify-content: center;
    align-items: center;
    gap: 6px;
    font-family: "EB Garamond", serif;
    font-size: 18px;
    color: var(--white);
    text-transform: uppercase;
    letter-spacing: 0.5px;
  }
  .address svg { width: 15px; height: 15px; flex: none; }
  .offer {
    font-family: "Barlow Condensed", sans-serif;
    font-style: italic;
    font-weight: 700;
    text-transform: uppercase;
    line-height: 1;
  }
  .offer-band {
    position: absolute;
    display: flex;
    align-items: center;
    justify-content: center;
    font-size: 32px;
  }
  .offer-band.green {
    left: 805px; top: 215px; width: 188px; height: 36px;
    background: var(--lime);
    color: var(--white);
  }
  .offer-band.black {
    left: 830px; top: 252px; width: 168px; height: 36px;
    background: var(--ink-black);
    color: var(--lime-bright);
  }
  .price-badge {
    position: absolute;
    left: 1006px;
    top: 233px;
    width: 78px;
    height: 78px;
  }
  .price-badge svg { position: absolute; inset: 0; }
  .price-value {
    position: absolute;
    inset: 0;
    display: flex;
    align-items: center;
    justify-content: center;
    color: var(--white);
    font-size: 34px;
  }
  .price-value sup { font-size: 17px; margin-top: -12px; }
</style>
</head>
<body>
  <section class="billboard">
    <div class="hero-photo" role="img" aria-label="Photograph of a realistic astronaut floating in space holding a green cannabis leaf, with planet Earth glowing blue behind"></div>

    <div class="headline-rule left"></div>
    <div class="rule-mark" role="img" aria-label="Small cannabis leaf ornament"></div>
    <div class="headline-rule right"></div>

    <h1 class="headline">
      <span class="line">Products</span>
      <span class="line">Out of This</span>
      <span class="accent">World</span>
    </h1>

    <div class="brand">
      <span class="brand-name">MARROWICK</span>
      <span class="brand-sub">CANNABIS COMPANY</span>
    </div>

    <p class="address">
      <svg viewBox="0 0 16 16" aria-hidden="true">
        <circle cx="8" cy="8" r="8" fill="var(--lime)"/>
        <path d="M8 3.5a3 3 0 0 0-3 3c0 2.2 3 5.5 3 5.5s3-3.3 3-5.5a3 3 0 0 0-3-3z" fill="none" stroke="#0b2a08" stroke-width="1.2"/>
        <circle cx="8" cy="6.5" r="1" fill="#0b2a08"/>
      </svg>
      871 Tallow Lane - Oswego
    </p>

    <div class="offer offer-band green">Free Delivery</div>
    <div class="offer offer-band black">Orders Over</div>

    <div class="price-badge offer">
      <svg viewBox="0 0 80 80" aria-hidden="true">
        <g fill="var(--lime)">
          <rect x="12" y="12" width="56" height="56"/>
          <rect x="12" y="12" width="56" height="56" transform="rotate(22.5 40 40)"/>
          <rect x="12" y="12" width="56" height="56" transform="rotate(45 40 40)"/>
          <rect x="12" y="12" width="56" height="56" transform="rotate(67.5 40 40)"/>
        </g>
        <line x1="20" y1="22" x2="60" y2="22" stroke="var(--white)" stroke-width="1"/>
        <line x1="20" y1="58" x2="60" y2="58" stroke="var(--white)" stroke-width="1"/>
      </svg>
      <span class="price-value"><sup>$</sup>150</span>
    </div>
  </section>
</body>
</html>
```